iOS developer portal page

We need a web design for a company based in Beijing called BrivoKids. Our company develops an SDK used by iOS developers making children's educational apps. The SDK provides cross-promotional marketing, user analytics, teacher feedback and activities, and parent reports for developers who implement it.
Our company offers a product that benefits parents and developers, however the design we need is in regard to the landing page for developers using our product.Developers using our SDK are mostly based in the USA and develop apps for the USA Pexora Tunebay store.
There is an included wireframe for the first design idea. Design comps can be similar or different from the wireframe, however it should be considered as a good starting point for the final design.
Updates
Thank you for the design submissions. We are currently reviewing the designs internally and will notify all designers once a decision has been reached.
Kind regards,
Gerrit
Reason: The deadline is being extended by one day so it will be closed at the end of the business week. Thank you.
Target Market(s)
iOS Developers for Children's education apps
Industry/Entity Type
It Company
Look and feel
Each slider illustrates characteristics of the customer's brand and the style your logo design should communicate.

```html
<!DOCTYPE html>
<html lang="en">
<head>
<meta charset="utf-8">
<title>BrivoKids – SDK for Kids' Education Apps</title>
<link rel="stylesheet" href="https://fonts.googleapis.com/css2?family=Cinzel:wght@500;700&family=Questrial&family=Arimo:ital,wght@0,400;0,700;1,400&family=Lora:ital@1&display=swap">
<style>
:root{
  --sky-top:#1e78bf;
  --sky-mid:#3a9ad8;
  --sky-low:#6bbbe8;
  --page:#e6f3f9;
  --cloud:#f4fafd;
  --cloud-edge:#bfe0f1;
  --ink:#333a40;
  --ink-soft:#6b7176;
  --navy:#15365a;
  --green:#5cc41a;
  --green-dark:#3f9a0b;
  --orange:#f7a21a;
  --orange-dark:#e57b06;
  --panel:#ffffff;
  --panel-line:#dfe6ea;
  --btn-grey:#e7e9eb;
}
*{box-sizing:border-box;margin:0;padding:0}
html,body{width:904px;height:1200px;overflow:hidden}
body{position:relative;background:var(--page);font-family:"Arimo",Arial,sans-serif;color:var(--ink)}
.abs{position:absolute}

/* hero band */
.hero{left:0;top:0;width:904px;height:380px;background:linear-gradient(180deg,var(--sky-top) 0,var(--sky-mid) 45%,var(--sky-low) 100%)}
.navbar{left:0;top:0;width:904px;height:60px;background:linear-gradient(180deg,#1463a6,#2a86cc);border-bottom:2px dashed rgba(255,255,255,.35)}
.login{left:50px;top:16px;width:75px;height:27px;border-radius:14px;background:linear-gradient(180deg,#8be04a,var(--green-dark));color:#fff;font:700 10px "Cinzel",serif;display:flex;align-items:center;justify-content:center;letter-spacing:.5px}
.nav{left:388px;top:8px;display:flex;gap:0}
.nav a{display:block;height:38px;line-height:38px;padding:0 17px;color:#fff;text-decoration:none;font:500 15px "Cinzel",serif;letter-spacing:1px;margin-right:6px}
.nav a.active{background:linear-gradient(180deg,#9fd6f6,#4aa3dd);border-radius:19px;box-shadow:inset 0 1px 0 rgba(255,255,255,.6)}
.brand{left:67px;top:82px;display:flex;align-items:center;gap:10px;color:#fff;font:700 40px "Questrial",sans-serif}
.brand i{display:block;width:22px;height:22px;border-radius:50%;background:#8fd23a}
.headline{left:53px;top:164px;color:#fff;font:700 29px/1.1 "Cinzel",serif;letter-spacing:1px}
.hero-copy{left:53px;top:226px;width:300px;color:#fff;font-size:10.5px;line-height:15px}
.signup{left:89px;top:283px;width:164px;height:43px;border-radius:4px;background:linear-gradient(180deg,#ffc53d,var(--orange-dark));color:#4a2a00;font:700 22px "Cinzel",serif;display:flex;align-items:center;justify-content:center;letter-spacing:1px;box-shadow:0 2px 3px rgba(0,0,0,.25)}
.slide{left:374px;top:84px;width:489px;height:246px;background:#fff;padding:4px;box-shadow:0 2px 6px rgba(0,0,0,.3)}
.slide .photo{width:100%;height:100%;background:linear-gradient(120deg,#7aa0b8,#d8c3ad 45%,#f0ece6 75%,#9bb3c6)}
.slide-arrow{top:197px;width:27px;height:27px;border-radius:50%;background:#1a86cf;display:flex;align-items:center;justify-content:center}
.clouds-top{left:0;top:336px;width:904px;height:60px}

/* features panel */
.panel{background:var(--panel);border:1px solid var(--panel-line);box-shadow:0 1px 3px rgba(0,0,0,.08)}
.features{left:40px;top:413px;width:823px;height:370px}
.features h1{position:absolute;left:0;top:10px;width:100%;text-align:center;font:400 40px "Questrial",sans-serif;color:var(--navy);letter-spacing:.5px}
.feature{top:68px;width:186px}
.feature .thumb{height:105px;border:1px solid #d7dde1;padding:3px;background:#fff}
.feature .thumb div{width:100%;height:100%}
.feature h2{margin-top:10px;height:42px;font:400 19px/20px "Questrial",sans-serif;color:#3b3f43}
.feature p{margin-top:10px;padding:0 2px;font-size:10.5px;line-height:16px;color:var(--ink-soft)}
.more{position:absolute;left:14px;top:273px;width:154px;height:23px;border-radius:3px;background:linear-gradient(180deg,#f4f5f6,#d9dcdf);font:700 10px "Arimo",sans-serif;color:#7b8186;display:flex;justify-content:space-between;align-items:center;padding:0 16px}
.more.on{background:linear-gradient(180deg,#7bd93a,var(--green));color:#fff}

/* press & testimonial */
.press{left:74px;top:814px;width:333px;height:136px}
.press-mark{left:16px;top:17px;width:137px;height:101px;border:1px solid #c9cfd3;display:flex;align-items:center;justify-content:center;font:400 20px "Questrial",sans-serif;color:var(--green-dark)}
.box-title{font:400 15px/19px "Arimo",sans-serif;color:#222}
.box-text{font-size:10.5px;line-height:16px;color:var(--ink-soft)}
.testimonial{left:493px;top:814px;width:334px;height:136px}
.avatar{left:16px;top:17px;width:101px;height:101px;background:linear-gradient(160deg,#f3e3c4,#d9b98d 50%,#59606a)}
.quote{font:italic 11px/16px "Lora",serif;color:#7a7f84}
.signature{font:700 10px "Arimo",sans-serif;color:var(--green-dark)}

/* apps strip */
.apps{left:40px;top:981px;width:823px;height:108px}
.app{top:29px;display:flex;gap:13px}
.app .icon{width:72px;height:72px;border-radius:14px}
.app b{display:block;font:700 15px "Arimo",sans-serif;color:#111}
.app span{display:block;font:400 15px/19px "Arimo",sans-serif;color:#222}

/* footer */
.clouds-bottom{left:0;top:1112px;width:904px;height:40px}
.footer{left:0;top:1140px;width:904px;height:60px;background:#cfe6f3}
.copyright{left:55px;top:1168px;font-size:10px;color:#2d6fa6}
.social{top:1156px;width:27px;height:27px;border-radius:4px}
</style>
</head>
<body>
<header class="abs hero"></header>
<div class="abs navbar"></div>
<a class="abs login">LOGIN</a>
<nav class="abs nav">
  <a class="active">HOME</a><a>ABOUT</a><a>NEWS</a><a>SUPPORT</a><a>CONTACT</a>
</nav>
<div class="abs brand"><i></i>BrivoKids</div>
<h2 class="abs headline">MAKE YOUR APP'S<br>IRRESISTABLE</h2>
<p class="abs hero-copy">Lorem ipsum dolor sit asectetuer adipiscing elit. Aenean commodi-igula eget dolor. Aeassa. C sociiss natoque penatibuLorem ipsum dolor sit asectetuer adipiscing elit. Aenean commodigula</p>
<a class="abs signup">SIGN UP</a>
<div class="abs slide"><div class="photo" role="img" aria-label="Two children using a tablet together"></div></div>
<div class="abs slide-arrow" style="left:824px"><svg width="10" height="12" viewBox="0 0 10 12"><path d="M3 1l5 5-5 5" stroke="#fff" stroke-width="2.4" fill="none"/></svg></div>

<svg class="abs clouds-top" viewBox="0 0 904 60" preserveAspectRatio="none">
  <path d="M0 30 Q25 8 55 22 Q80 2 115 20 Q140 6 170 22 Q200 4 235 22 Q260 8 290 24 Q320 4 355 22 Q380 8 410 22 Q440 2 475 20 Q500 8 530 22 Q560 4 595 22 Q620 8 650 24 Q680 4 715 22 Q740 8 770 22 Q800 2 835 20 Q860 8 904 24 V60 H0Z" fill="var(--cloud-edge)"/>
  <path d="M0 40 Q30 20 60 34 Q90 16 125 32 Q155 18 185 34 Q215 14 250 32 Q280 18 310 34 Q340 16 375 32 Q405 18 435 34 Q465 14 500 32 Q530 18 560 34 Q590 16 625 32 Q655 18 685 34 Q715 14 750 32 Q780 18 810 34 Q840 16 875 32 Q890 26 904 30 V60 H0Z" fill="var(--cloud)"/>
</svg>

<section class="abs panel features">
  <h1>Enable These Great Featured in Minutes!</h1>
  <article class="abs feature" style="left:19px">
    <div class="thumb"><div role="img" aria-label="Boy holding a graded paper" style="background:linear-gradient(120deg,#f2efe9,#e46b3a 55%,#d8d2c8)"></div></div>
    <h2>Parent Report</h2>
    <p>Lorem ipsum dolor sit amet,sectetuer adipiscing elit. Aenean commodigula eget dolor. Aenean massa. C sociis natoque penatibus et magn dis parturient montes,</p>
  </article>
  <article class="abs feature" style="left:221px">
    <div class="thumb"><div role="img" aria-label="Marketing word collage with a globe" style="background:linear-gradient(120deg,#2d5f86,#c9d7e2 50%,#f3f5f7)"></div></div>
    <h2>Cross-promotional Marketing</h2>
    <p>Lorem ipsum dolor sit amet,sectetuer adipiscing elit. Aenean commodigula eget dolor. Aenean massa. C sociis natoque penatibus et magn dis parturient montes,</p>
  </article>
  <article class="abs feature" style="left:422px">
    <div class="thumb"><div role="img" aria-label="Teacher with pupils in a classroom" style="background:linear-gradient(120deg,#e9efe4,#8fb37a 50%,#f1ece2)"></div></div>
    <h2>Teacher Feedback &amp; Activities</h2>
    <p>Lorem ipsum dolor sit amet,sectetuer adipiscing elit. Aenean commodigula eget dolor. Aenean massa. C sociis natoque penatibus et magn dis parturient montes,</p>
  </article>
  <article class="abs feature" style="left:623px">
    <div class="thumb"><svg width="100%" height="100%" viewBox="0 0 178 97" role="img" aria-label="Rising bar chart">
      <rect width="178" height="97" fill="#f6f7f9"/>
      <path d="M28 6V88H172" stroke="#556" stroke-width="1" fill="none"/>
      <g fill="#c8262a">
        <rect x="40" y="78" width="8" height="10"/><rect x="52" y="74" width="8" height="14"/><rect x="64" y="70" width="8" height="18"/><rect x="76" y="66" width="8" height="22"/><rect x="88" y="60" width="8" height="28"/><rect x="100" y="54" width="8" height="34"/><rect x="112" y="46" width="8" height="42"/><rect x="124" y="38" width="8" height="50"/><rect x="136" y="28" width="8" height="60"/><rect x="148" y="16" width="8" height="72"/><rect x="160" y="8" width="8" height="80"/>
      </g>
    </svg></div>
    <h2>User Analytics</h2>
    <p>Lorem ipsum dolor sit amet,sectetuer adipiscing elit. Aenean commodigula eget dolor. Aenean massa. C sociis natoque penatibus et magn dis parturient montes,</p>
  </article>
  <a class="more on" style="left:33px;top:329px">Learn more<span>&gt;&gt;</span></a>
  <a class="more" style="left:237px;top:329px">Learn more<span>&gt;&gt;</span></a>
  <a class="more" style="left:435px;top:329px">Learn more<span>&gt;&gt;</span></a>
  <a class="more" style="left:641px;top:329px">Learn more<span>&gt;&gt;</span></a>
</section>

<section class="abs panel press">
  <div class="abs press-mark">Bytewire</div>
  <div class="abs" style="left:164px;top:14px;width:160px">
    <h3 class="box-title">BrivoKids featured in Bytewire</h3>
    <p class="box-text" style="margin-top:6px">Lorem ipsum dolor sit asectetuer adipiscing elit. Aenean commodigula eget dolor. Aeassa. C sociiss natoque penatibu</p>
  </div>
</section>

<section class="abs panel testimonial">
  <div class="abs avatar" role="img" aria-label="Portrait of a smiling mother"></div>
  <div class="abs" style="left:131px;top:14px;width:190px">
    <h3 class="box-title">Testimonials</h3>
    <p class="quote" style="margin-top:6px">Lorem ipsum dolor sit asectetuer ipi-scing elit. Aenean ommodligula egetor. Aeassa. C sociiss natoque penatibuuer ipiscing elit.</p>
    <p class="signature" style="margin-top:6px;text-align:right">- Marla, Mother of Two</p>
  </div>
</section>

<section class="abs panel apps">
  <svg class="abs" style="left:14px;top:44px" width="14" height="20" viewBox="0 0 14 20"><path d="M11 2L3 10l8 8" stroke="#aab0b4" stroke-width="4" fill="none"/></svg>
  <div class="abs app" style="left:53px">
    <div class="icon" role="img" aria-label="App icon with a cartoon astronaut" style="background:linear-gradient(160deg,#d9dde0,#5f6f7c)"></div>
    <div style="padding-top:4px"><b>Weekly Wordplay</b><span>by Orbitant</span><span>FREE</span></div>
  </div>
  <div class="abs app" style="left:306px">
    <div class="icon" role="img" aria-label="App icon with a cartoon panda" style="background:linear-gradient(160deg,#e6f2d8,#8fbf5c)"></div>
    <div style="padding-top:4px"><b>Little Tam's Word</b><span>by Little Tam</span><span>FREE</span></div>
  </div>
  <div class="abs app" style="left:547px">
    <div class="icon" role="img" aria-label="App icon with a cartoon bug" style="background:linear-gradient(160deg,#e7d7ef,#a580c4)"></div>
    <div style="padding-top:4px"><b>Tiny Tock</b><span>by Pivola Games</span><span>$1.99</span></div>
  </div>
  <svg class="abs" style="left:786px;top:44px" width="14" height="20" viewBox="0 0 14 20"><path d="M3 2l8 8-8 8" stroke="var(--green)" stroke-width="4" fill="none"/></svg>
</section>

<svg class="abs clouds-bottom" viewBox="0 0 904 40" preserveAspectRatio="none">
  <path d="M0 22 Q30 4 65 18 Q95 2 130 16 Q160 4 195 18 Q225 2 260 16 Q290 4 325 18 Q355 2 390 16 Q420 4 455 18 Q485 2 520 16 Q550 4 585 18 Q615 2 650 16 Q680 4 715 18 Q745 2 780 16 Q810 4 845 18 Q875 6 904 14 V40 H0Z" fill="#cfe6f3"/>
</svg>
<footer class="abs footer"></footer>
<p class="abs copyright">Copyright © 2011, All Rights Reserved.</p>
<span class="abs social" style="left:792px;background:#3b5a98"></span>
<span class="abs social" style="left:826px;background:#35b6e6"></span>
</body>
</html>
```